Saffron Ledger Works Flyer

We need a one page promotional piece that explains what our company does, and the benefits it provides in a simple, elegant, easy to understand way. I would like to print it on glossy heavyweight paper to give a feel of high quality and legitimacy. I will include the logo, the tag line, and the main benefits that the company offers.

Tag line concept, may not need these exact words. "Give us 5 minutes a day, and we will help you build a Saffron Ledger Works."

Key points...(exact wording not required if you think of a better way to say it)

Software easy enough for my grandpa to use.
Lets you use snail mail, email, texting, and social media to quickly market to your customers at very low cost.
Web based which allows you to launch media campaigns from your desktop, or smartphone in moments.
Quick 3 - 5 minute training videos which give you hard hitting, quick action tips that will help you make your business better today.
Live coaching calls to help motivate you to improve your business.
No contracts, or start up fees. One low price of $299 per month.

Restaurant owners

Restaurant

```html
<!DOCTYPE html>
<html lang="en">
<head>
<meta charset="utf-8">
<title>Saffron Ledger Works Flyer</title>
<link href="https://fonts.googleapis.com/css2?family=Arimo:wght@400;700&family=Roboto+Condensed:wght@700&display=swap" rel="stylesheet">
<style>
  :root {
    --sky-top: #a6c4e7;
    --sky-mid: #c3daf0;
    --sky-glow: #e2eef9;
    --brand-grey: #7b7b7b;
    --banner-blue: #0b3fae;
    --banner-blue-dark: #062f8c;
    --ink: #111111;
    --navy: #0c1c6b;
    --paper: #ffffff;
  }
  * { margin: 0; padding: 0; box-sizing: border-box; }
  html, body { width: 846px; height: 1200px; overflow: hidden; }
  body { font-family: "Arimo", Arial, sans-serif; background: var(--sky-top); }

  .flyer {
    position: relative;
    width: 846px;
    height: 1200px;
    overflow: hidden;
    background:
      radial-gradient(ellipse 520px 420px at 430px 900px, var(--sky-glow) 0%, rgba(226,238,249,0) 75%),
      linear-gradient(180deg, var(--sky-top) 0%, var(--sky-top) 40%, var(--sky-mid) 70%, var(--sky-top) 100%);
  }

  .brand {
    position: absolute;
    top: 40px;
    left: 0;
    width: 846px;
    display: flex;
    flex-direction: column;
    align-items: center;
  }
  .brand-mark {
    width: 230px;
    height: 230px;
    border-radius: 50%;
    background: #e4e9ee;
    margin-bottom: 48px;
  }
  .brand-name {
    font-family: "Arimo", Arial, sans-serif;
    font-weight: 700;
    color: var(--brand-grey);
    text-align: center;
    font-size: 42px;
    line-height: 44px;
    letter-spacing: 2px;
    text-transform: uppercase;
  }

  .tagline {
    position: absolute;
    left: 25px;
    top: 497px;
    width: 805px;
    height: 118px;
    background: linear-gradient(180deg, var(--banner-blue) 0%, var(--banner-blue-dark) 100%);
    border: 2px solid rgba(255,255,255,0.6);
    display: flex;
    align-items: center;
    justify-content: center;
    padding: 0 14px;
  }
  .tagline-tail {
    position: absolute;
    left: 36px;
    top: 613px;
  }
  .tagline p {
    font-family: "Roboto Condensed", "Arial Narrow", sans-serif;
    font-weight: 700;
    color: var(--paper);
    text-transform: uppercase;
    text-align: center;
    font-size: 35px;
    line-height: 42px;
    letter-spacing: -0.5px;
  }

  .headline {
    position: absolute;
    top: 658px;
    left: 0;
    width: 846px;
    text-align: center;
    font-weight: 700;
    font-size: 23px;
    letter-spacing: 1.6px;
    color: var(--ink);
    text-transform: uppercase;
  }

  .benefits { list-style: none; }
  .benefit {
    position: absolute;
    left: 65px;
    width: 764px;
    font-weight: 700;
    font-size: 19px;
    line-height: 29px;
    color: var(--ink);
    text-transform: uppercase;
    text-align: justify;
    letter-spacing: 0.3px;
  }
  .benefit::before {
    content: "";
    position: absolute;
    left: -42px;
    top: 6px;
    width: 20px;
    height: 20px;
    border-radius: 50%;
    background: var(--ink);
  }
  .benefit-channels { top: 719px; }
  .benefit-web { top: 805px; }
  .benefit-videos { top: 890px; }
  .benefit-coaching { top: 1003px; }

  .pricing {
    position: absolute;
    left: 25px;
    top: 1092px;
    width: 805px;
    height: 96px;
    background: var(--paper);
    text-align: center;
    color: var(--navy);
    padding-top: 8px;
  }
  .pricing-notch {
    position: absolute;
    right: 16px;
    top: 1070px;
  }
  .price {
    font-weight: 700;
    font-size: 40px;
    line-height: 44px;
  }
  .terms {
    font-weight: 700;
    font-size: 29px;
    line-height: 36px;
    letter-spacing: 3.4px;
  }
</style>
</head>
<body>
  <main class="flyer">
    <header class="brand">
      <div class="brand-mark" aria-hidden="true"></div>
      <h1 class="brand-name">Saffron<br>Ledger<br>Works</h1>
    </header>

    <section class="tagline">
      <p>"Give us 5 minutes a day, and we will help you build a Saffron Ledger Works."</p>
    </section>
    <svg class="tagline-tail" width="36" height="24" viewBox="0 0 36 24" aria-hidden="true">
      <polygon points="0,0 36,0 0,24" fill="#062f8c"/>
    </svg>

    <h2 class="headline">Software easy enough for my grandpa to use</h2>

    <ul class="benefits">
      <li class="benefit benefit-channels">Lets you use snail mail, email, texting, and social media to quickly market to your customers at very low cost.</li>
      <li class="benefit benefit-web">Web based which allows you to launch media campaigns from your desktop, or smartphone in moments.</li>
      <li class="benefit benefit-videos">Quick 3 - 5 minute training videos which give you hard hitting, quick action tips that will help you make your business better today.</li>
      <li class="benefit benefit-coaching">Live coaching calls to help motivate you to improve your business.</li>
    </ul>

    <svg class="pricing-notch" width="40" height="24" viewBox="0 0 40 24" aria-hidden="true">
      <polygon points="20,0 40,24 0,24" fill="#ffffff"/>
    </svg>
    <section class="pricing">
      <p class="price">ONE LOW PRICE OF $299 PER MONTH</p>
      <p class="terms">NO CONTRACTS, OR START UP FEES</p>
    </section>
  </main>
</body>
</html>
```